Spy/Espionage/Counterintelligence Membership Community Needs a PowerPoint Template

We need a powerpoint template for one of our business verticals focused on spies, espionage, and counterintelligence. The name of it is "Pale Harbor Guild" and the logo is attached. Pale Harbor Guild is a community that connects people with experts in espionage and counterintelligence through an online social network, as well as in-person events. We would like to see designs that incorporate the red and black of the logo. The design should communicate mystery/suspense and peak curiosity.

Target Market(s)

Late 20s to baby boomers, male

Industry/Entity Type

Social Club

Font styles to use
Sans Serif

Colors
ec1f27
000000
ffffff

Requirements
Must have
• A user-friendly ppt template file. Incorporate basic fonts that don't have to be installed on every computer for presentations. A cover slide and a basic inside slide. A white background. I will also need graphic source files.
Nice to have
• Plenty of space for slide title and body content. Logo on every slide.
Should not have
• Inconsistency with fonts. Misalignment of images.

```html
<!DOCTYPE html>
<html lang="en">
<head>
<meta charset="utf-8">
<title>Pale Harbor Guild – Inside Slide</title>
<link rel="stylesheet" href="https://fonts.googleapis.com/css2?family=Questrial&family=Open+Sans:wght@400;600;700&display=swap">
<style>
  :root {
    --brand-red: #c4000b;
    --ink: #1a1a1a;
    --white: #ffffff;
    --tab-dark: #6c6c6c;
    --tab-light: #8a8a8a;
    --body-grey: #9a9a9a;
    --heading-grey: #8c8c8c;
    --halo: #ececec;
  }
  html, body { margin: 0; padding: 0; overflow: hidden; background: var(--white); }
  .slide {
    position: relative; width: 1200px; height: 900px; overflow: hidden;
    background: var(--white); font-family: "Open Sans", Arial, sans-serif;
  }
  .header {
    position: absolute; left: 0; top: 0; width: 1200px; height: 75px;
    background: var(--brand-red); border-bottom: 3px solid var(--white);
    box-shadow: 0 4px 0 -1px var(--ink);
  }
  .slide-title {
    position: absolute; left: 20px; top: 10px; margin: 0;
    font-family: "Questrial", "Century Gothic", sans-serif; font-weight: 400;
    font-size: 44px; color: var(--white); letter-spacing: 0.3px;
  }
  .brand {
    position: absolute; right: 14px; top: 14px; display: flex; align-items: center; gap: 10px;
    font-family: "Questrial", "Century Gothic", sans-serif; font-size: 31px; color: var(--ink);
  }
  .brand-dot { width: 40px; height: 40px; border-radius: 50%; border: 4px solid var(--ink); box-sizing: border-box; }
  .halo {
    position: absolute; left: -45px; top: 196px; width: 540px; height: 540px;
    border-radius: 50%; background: var(--halo); opacity: 0.75;
  }
  .topic { position: absolute; left: 0; width: 1200px; height: 128px; }
  .topic-tab { position: absolute; left: 0; top: 0; }
  .topic-text { position: absolute; left: 255px; top: 4px; width: 810px; }
  .topic-heading {
    margin: 0; font-size: 24px; font-weight: 600; color: var(--brand-red); line-height: 1.3;
  }
  .topic-heading span { color: var(--heading-grey); }
  .topic-body {
    margin: 4px 0 0 4px; font-size: 15.5px; line-height: 22.5px; color: var(--body-grey);
  }
  .footer {
    position: absolute; left: 0; bottom: 0; width: 1200px; height: 44px; background: var(--ink);
  }
  .copyright {
    position: absolute; left: 10px; top: 10px; margin: 0;
    font-family: "Questrial", "Century Gothic", sans-serif; font-size: 20px; color: var(--white);
  }
  .page-number {
    position: absolute; right: 8px; top: 5px; width: 32px; height: 32px; box-sizing: border-box;
    border-radius: 50%; background: var(--brand-red); border: 2px solid var(--white);
    color: var(--white); font-size: 17px; line-height: 28px; text-align: center;
  }
</style>
</head>
<body>
<div class="slide">
  <div class="halo"></div>

  <header class="header">
    <h1 class="slide-title">Project Title Here</h1>
    <div class="brand"><span class="brand-dot"></span>Pale Harbor Guild</div>
  </header>

  <svg width="0" height="0" style="position:absolute">
    <defs>
      <linearGradient id="tabFill" x1="0" y1="0" x2="1" y2="0">
        <stop offset="0" stop-color="#6a6a6a"/>
        <stop offset="1" stop-color="#858585"/>
      </linearGradient>
    </defs>
  </svg>

  <section class="topic" style="top:153px">
    <svg class="topic-tab" width="232" height="128" viewBox="0 0 232 128">
      <polygon points="0,0 212,0 230,64 212,128 0,128" fill="url(#tabFill)"/>
      <g fill="none" stroke="#fff" stroke-width="3" stroke-linecap="round">
        <path d="M108 88 C108 76 96 70 96 54 a24 24 0 1 1 48 0 C144 70 132 76 132 88 Z"/>
        <path d="M112 88 L112 66 M128 88 L128 66 M112 66 c0-8 8-12 8-4 c0 -8 8 -4 8 4"/>
        <line x1="108" y1="95" x2="132" y2="95"/><line x1="110" y1="102" x2="130" y2="102"/>
        <line x1="114" y1="109" x2="126" y2="109"/>
      </g>
    </svg>
    <div class="topic-text">
      <h2 class="topic-heading">TEXT HEADING <span>HERE</span></h2>
      <p class="topic-body">Lorem ipsum dolor sit Lorem ipsum dolor sit&nbsp; Lorem ipsum dolor sit Lorem ipsum dolor sit&nbsp; Lorem ipsum dolor sit Lorem ipsum dolor&nbsp; Lorem ipsum dolor sit Lorem ipsum dolor sit&nbsp; Lorem ipsum dolor sit Lorem ipsum dolor sit&nbsp; Lorem ipsum dolor sit Lorem ipsum dolor&nbsp; Lorem ipsum dolor sit Lorem ipsum dolor sit&nbsp; Lorem ipsum dolor sit Lorem ipsum dolor sit</p>
    </div>
  </section>

  <section class="topic" style="top:315px">
    <svg class="topic-tab" width="232" height="128" viewBox="0 0 232 128">
      <polygon points="0,0 212,0 230,64 212,128 0,128" fill="url(#tabFill)"/>
      <g fill="#fff">
        <path d="M120 20 C108 34 108 52 116 66 L124 66 C132 52 132 34 120 20 Z"/>
        <path d="M114 66 C100 52 80 58 82 74 C84 86 98 86 98 76 C92 80 88 74 92 70 C98 64 108 70 112 76 Z"/>
        <path d="M126 66 C140 52 160 58 158 74 C156 86 142 86 142 76 C148 80 152 74 148 70 C142 64 132 70 128 76 Z"/>
        <rect x="100" y="74" width="40" height="7" rx="2"/>
        <path d="M114 81 L126 81 L124 100 L136 108 L104 108 L116 100 Z"/>
      </g>
    </svg>
    <div class="topic-text">
      <h2 class="topic-heading">TEXT HEADING <span>HERE</span></h2>
      <p class="topic-body">Lorem ipsum dolor sit Lorem ipsum dolor sit&nbsp; Lorem ipsum dolor sit Lorem ipsum dolor sit&nbsp; Lorem ipsum dolor sit Lorem ipsum dolor&nbsp; Lorem ipsum dolor sit Lorem ipsum dolor sit&nbsp; Lorem ipsum dolor sit Lorem ipsum dolor sit&nbsp; Lorem ipsum dolor sit Lorem ipsum dolor&nbsp; Lorem ipsum dolor sit Lorem ipsum dolor sit&nbsp; Lorem ipsum dolor sit Lorem ipsum dolor sit</p>
    </div>
  </section>

  <section class="topic" style="top:477px">
    <svg class="topic-tab" width="232" height="128" viewBox="0 0 232 128">
      <polygon points="0,0 212,0 230,64 212,128 0,128" fill="url(#tabFill)"/>
      <g fill="none" stroke="#fff" stroke-width="8">
        <circle cx="120" cy="64" r="36"/>
        <line x1="95" y1="39" x2="145" y2="89"/>
      </g>
    </svg>
    <div class="topic-text">
      <h2 class="topic-heading">TEXT HEADING <span>HERE</span></h2>
      <p class="topic-body">Lorem ipsum dolor sit Lorem ipsum dolor sit&nbsp; Lorem ipsum dolor sit Lorem ipsum dolor sit&nbsp; Lorem ipsum dolor sit Lorem ipsum dolor&nbsp; Lorem ipsum dolor sit Lorem ipsum dolor sit&nbsp; Lorem ipsum dolor sit Lorem ipsum dolor sit&nbsp; Lorem ipsum dolor sit Lorem ipsum dolor&nbsp; Lorem ipsum dolor sit Lorem ipsum dolor sit&nbsp; Lorem ipsum dolor sit Lorem ipsum dolor sit</p>
    </div>
  </section>

  <section class="topic" style="top:639px">
    <svg class="topic-tab" width="232" height="128" viewBox="0 0 232 128">
      <polygon points="0,0 212,0 230,64 212,128 0,128" fill="url(#tabFill)"/>
      <g fill="none" stroke="#fff" stroke-width="2">
        <circle cx="120" cy="64" r="22"/>
        <line x1="72" y1="64" x2="168" y2="64"/>
        <line x1="120" y1="16" x2="120" y2="112"/>
      </g>
      <circle cx="120" cy="64" r="10" fill="#fff"/>
    </svg>
    <div class="topic-text">
      <h2 class="topic-heading">TEXT HEADING <span>HERE</span></h2>
      <p class="topic-body">Lorem ipsum dolor sit Lorem ipsum dolor sit&nbsp; Lorem ipsum dolor sit Lorem ipsum dolor sit&nbsp; Lorem ipsum dolor sit Lorem ipsum dolor&nbsp; Lorem ipsum dolor sit Lorem ipsum dolor sit&nbsp; Lorem ipsum dolor sit Lorem ipsum dolor sit&nbsp; Lorem ipsum dolor sit Lorem ipsum dolor&nbsp; Lorem ipsum dolor sit Lorem ipsum dolor sit&nbsp; Lorem ipsum dolor sit Lorem ipsum dolor sit</p>
    </div>
  </section>

  <footer class="footer">
    <p class="copyright">Copyright text here</p>
    <div class="page-number">1</div>
  </footer>
</div>
</body>
</html>
```